Document Processing Services and Solutions for School Systems

I am looking to design a brochure for both Digital and Paper use. I can supply the written content. Would be looking for an overall design of the brochure with provided content worked into it.

```html
<!DOCTYPE html>
<html lang="en">
<head>
<meta charset="utf-8">
<title>Northgate Systems – School Document Management Flyer</title>
<link rel="stylesheet" href="https://fonts.googleapis.com/css2?family=Anton&family=Ubuntu:wght@400;500;700&display=swap">
<style>
  :root{
    --gold:#C99A2E;
    --navy:#2E3690;
    --white:#ffffff;
    --ink:#55565c;
    --stage:#e3e4ea;
    --photo-warm:#b07a52;
    --photo-dark:#3a2b28;
    --photo-light:#e9ddcf;
  }
  *{box-sizing:border-box;margin:0;padding:0}
  html,body{width:1200px;height:856px;overflow:hidden;background:var(--stage)}
  .flyer{position:absolute;left:303px;top:18px;width:594px;height:820px;background:var(--white);overflow:hidden;font-family:"Ubuntu",sans-serif;box-shadow:0 2px 8px rgba(0,0,0,.12)}
  .hero-photo{position:absolute;left:0;top:0;width:594px;height:256px;
    background:linear-gradient(120deg,var(--photo-light) 0%,var(--photo-warm) 38%,var(--photo-dark) 70%,#1f1b22 100%)}
  .brand{position:absolute;left:18px;top:52px;display:flex;align-items:center;gap:8px}
  .brand-mark{width:12px;height:12px;background:var(--gold)}
  .brand-name{font-family:"Ubuntu",sans-serif;font-weight:700;font-size:25px;color:var(--navy);letter-spacing:.2px}
  .headline-block{position:absolute;left:0;top:213px;width:278px;height:173px;background:var(--gold);border-bottom-right-radius:70px;z-index:2}
  .headline{font-family:"Anton",sans-serif;font-weight:400;color:var(--white);font-size:25.5px;line-height:30.5px;padding:14px 0 0 22px;letter-spacing:.2px}
  .intro-block{position:absolute;left:250px;top:254px;width:344px;height:132px;background:var(--navy);border-bottom-right-radius:60px;padding:9px 18px 0 38px;color:var(--white)}
  .intro-title{font-family:"Anton",sans-serif;font-weight:400;font-size:19px;line-height:24px;letter-spacing:.2px}
  .intro-text{font-size:11.6px;line-height:12.7px;font-weight:500;text-align:justify;margin-top:5px}
  .tab{position:absolute;top:386px;height:56px;font-family:"Anton",sans-serif;font-weight:400;font-size:21px;display:flex;align-items:center}
  .tab-services{left:0;width:206px;background:var(--navy);color:var(--gold);border-top-right-radius:40px;border-bottom-right-radius:40px;padding-left:20px}
  .tab-why{left:359px;width:215px;background:var(--gold);color:var(--white);border-bottom-left-radius:44px;justify-content:flex-end;padding-right:10px}
  .services{position:absolute;left:18px;top:446px;width:305px}
  .service{margin-bottom:3px}
  .service-title{display:flex;align-items:center;gap:5px;color:var(--gold);font-weight:500;font-size:16.3px;line-height:19px}
  .mark{display:inline-block;width:18px;height:18px;background:var(--navy);flex:none}
  .service ul{list-style:none;margin:1px 0 0 30px}
  .service li{position:relative;font-size:11.2px;line-height:12.6px;color:var(--ink);margin-bottom:0}
  .service li::before{content:"";position:absolute;left:-14px;top:4px;width:7px;height:7px;border-radius:50%;background:var(--navy)}
  .why-list{position:absolute;left:357px;top:447px;width:237px}
  .why-item{position:relative;height:50px;margin-bottom:3px}
  .why-item .mark{position:absolute;left:0;top:10px;width:20px;height:20px;background:var(--gold)}
  .why-box{position:absolute;left:26px;top:0;width:211px;height:50px;background:var(--navy);padding:3px 0 0 20px}
  .why-title{color:var(--gold);font-weight:500;font-size:16.5px;line-height:18px}
  .why-text{color:var(--white);font-weight:500;font-size:10.6px;line-height:11.8px;margin-top:2px}
  .cta{position:absolute;left:327px;top:661px;width:267px;height:80px;background:var(--gold);border-top-left-radius:54px;padding:10px 0 0 55px}
  .cta-title{font-family:"Anton",sans-serif;font-weight:400;color:var(--navy);font-size:22px;line-height:26px;letter-spacing:.3px}
  .cta-text{color:var(--white);font-weight:700;font-size:12.3px;line-height:16px}
  .contact-band{position:absolute;left:0;top:741px;width:594px;height:43px;background:var(--navy);color:var(--white);font-weight:500;font-size:14.3px;line-height:16.5px;text-align:center;padding-top:5px}
  .footer{position:absolute;left:0;top:784px;width:594px;height:36px;background:var(--gold);display:flex;align-items:center;justify-content:center;gap:5px;color:var(--white);font-weight:700;font-size:15px}
  .footer .icon{width:15px;height:15px;flex:none}
  .footer span+svg{margin-left:6px}
</style>
</head>
<body>
<main class="flyer">
  <div class="hero-photo" role="img" aria-label="Photo of students working together over open books and papers at a desk"></div>

  <div class="brand">
    <span class="brand-mark"></span>
    <span class="brand-name">Northgate Systems Inc</span>
  </div>

  <section class="intro-block">
    <h2 class="intro-title">Streamline, Secure, and Simplify</h2>
    <p class="intro-text">Managing school documents efficiently is crucial for smooth operations, compliance, and productivity. Our document processing services provide innovative solutions tailored for educational institutions, ensuring secure and seamless document and data handling.</p>
  </section>

  <section class="headline-block">
    <h1 class="headline">Transform Your School’s Document Management with Our Comprehensive Solutions</h1>
  </section>

  <div class="tab tab-services">Our Services</div>
  <div class="tab tab-why">Why Choose Us?</div>

  <section class="services">
    <div class="service">
      <h3 class="service-title"><span class="mark"></span>Document Scanning &amp; Conversion</h3>
      <ul>
        <li>Convert paper records into digital formats for easy access and storage.</li>
        <li>High-speed scanning for student records, administrative files, and historical archives.</li>
        <li>OCR (Optical Character Recognition) for searchable and editable documents.</li>
      </ul>
    </div>
    <div class="service">
      <h3 class="service-title"><span class="mark"></span>Cloud-Based Document Management</h3>
      <ul>
        <li>Secure, centralized document storage accessible from anywhere.</li>
        <li>Role-based access controls for administrators, teachers, and staff.</li>
        <li>Automated backups and compliance with educational data security standards.</li>
      </ul>
    </div>
    <div class="service">
      <h3 class="service-title"><span class="mark"></span>Workflow Automation</h3>
      <ul>
        <li>Digitize and streamline approval processes for enrollment, transcripts, and HR forms.</li>
        <li>Reduce paperwork and improve efficiency with automated workflows.</li>
        <li>Integration capable with existing school management systems.</li>
      </ul>
    </div>
  </section>

  <section class="why-list">
    <div class="why-item"><span class="mark"></span><div class="why-box"><h3 class="why-title">Increased Efficiency</h3><p class="why-text">– Save time with digital work flows and instant document retrieval.</p></div></div>
    <div class="why-item"><span class="mark"></span><div class="why-box"><h3 class="why-title">Enhanced Security</h3><p class="why-text">– Protect sensitive student and faculty information.</p></div></div>
    <div class="why-item"><span class="mark"></span><div class="why-box"><h3 class="why-title">Cost Savings</h3><p class="why-text">– Reduce paper, printing, and storage costs.</p></div></div>
    <div class="why-item"><span class="mark"></span><div class="why-box"><h3 class="why-title">Eco-Friendly</h3><p class="why-text">– Minimize your school’s carbon footprint by going digital.</p></div></div>
  </section>

  <section class="cta">
    <h2 class="cta-title">Get Started Today!</h2>
    <p class="cta-text">Let us help you modernize your document processing system.</p>
  </section>

  <p class="contact-band">Contact us for a free consultation and discover how our solutions can<br>transform your school's document management.</p>

  <footer class="footer">
    <svg class="icon" viewBox="0 0 16 16" aria-hidden="true"><circle cx="8" cy="8" r="8" fill="#2E3690"/><path d="M5.2 4.2l1.6-.3.8 2-1 .8a6 6 0 0 0 2.7 2.7l.8-1 2 .8-.3 1.6c-3.5.4-7-3.1-6.6-6.6z" fill="#fff"/></svg>
    <span>555-014-2290</span>
    <svg class="icon" viewBox="0 0 16 16" aria-hidden="true"><circle cx="8" cy="8" r="8" fill="#2E3690"/><rect x="4" y="5" width="8" height="6" rx="1" fill="none" stroke="#fff" stroke-width="1.2"/><path d="M4.3 5.4L8 8.3l3.7-2.9" fill="none" stroke="#fff" stroke-width="1.2"/></svg>
    <span>info@northgatedocs.com</span>
    <svg class="icon" viewBox="0 0 16 16" aria-hidden="true"><circle cx="8" cy="8" r="8" fill="#2E3690"/><circle cx="8" cy="8" r="4.5" fill="none" stroke="#fff" stroke-width="1"/><ellipse cx="8" cy="8" rx="2" ry="4.5" fill="none" stroke="#fff" stroke-width="1"/><path d="M3.5 8h9" stroke="#fff" stroke-width="1"/></svg>
    <span>www.northgatedocs.com</span>
  </footer>
</main>
</body>
</html>
```